Pivots & Treads .com

This website is simple!!!
Landing page background image should capture the customers attention!!! We will provide a image as a example of what we like. The purpose for this website is to provide customers with a clean easy way to request a quote for industrial casters and wheels by OEM’s as well as maintenance departments worldwide. Please see if you can follow our thought process below.
Customer comes to website, they are invited to Request a Quote by providing us with Manufacturer Name, Manufacturers Part # and quantity needed.
If this is not known the customer will complete will WP conversation format form answering about 10 questions
Or
Look up the part number in one of the 8 to 12 catalogs located in the Flippin Book format on our catalog page, or equal plug in .
When the client request a quote a account page will pop up request The following:
Clients first and last name
Email address
And optional questions
Company name and best contact number.
Once this is complete customer will hit SUBMIT.
The customers request will be in system. A email will be sent to Customer service notifying us the Quote Request has been made.
We will then build a quote for the customer with a good, better and best options. Customers Request a Quote submission may have more than one caster or wheel requested at a time, so website must allow this.
When the customer comes back into website there email address will come up as the account name and request a password be made for them. This will allow them to store quotes in their account for future needs. If quote is older than 30 day the system will trigger a button at the bottom of the quote for resubmit Request for updated quote.
Once customer reviews quote the quote can be Converted to order within the website.
Once Converted the system will send us a email and order will be processed.
We will need a Chat program that will text to CS the questions.
You will need to have high quality graphic design skills on your team.
We have found 2 plugins that would work nicely with our new website Flippin books to showcase our catalogs for customers to research and WPForms conversation forms to complete request for quote form.
Just Ideas:
Very very ghosted caster blueprint in white background but very very ghosted or the icon just idea
We have never had a font used we like
Grayscale every except for rubber on wheels and logo icon
Website should have hamburger menu on left
Website should hav responsive deign
Account head on right side
Has anyone read the brief from top to bottom and the updates, I’m seeing a lot of duplicates of the website I posted in images I want a clean website With lite backgrand with the poly being definite colors on each wheel I added a green yellow and red image has anyone looked at that Just a question?
Went on vacation/holiday

```html
<!DOCTYPE html>
<html lang="en">
<head>
<meta charset="UTF-8">
<title>Pivots &amp; Treads .com – Request a Quote</title>
<link rel="stylesheet" href="https://fonts.googleapis.com/css2?family=Montserrat:ital,wght@0,400;0,500;0,600;0,700;0,800;1,400&display=swap">
<style>
  :root {
    --ink-dark: #1b2233;
    --ink-muted: #4d5567;
    --ink-white: #ffffff;
    --accent-blue: #0a7cf2;
    --accent-outline: #1f7ef0;
    --scene-top: #f4f5f7;
    --scene-mid: #e9ebef;
    --scene-floor: #d9dce1;
    --line-soft: #9aa2b1;
    --footer-bg: #000000;
    --product-navy: #2c3b68;
    --product-steel: #b6bcc6;
    --product-iron: #2b2b2e;
  }
  * { box-sizing: border-box; margin: 0; padding: 0; }
  html, body {
    width: 1200px; height: 651px; overflow: hidden;
    font-family: "Montserrat", sans-serif;
    color: var(--ink-dark);
  }
  .page { position: relative; width: 1200px; height: 651px; overflow: hidden; }

  .hero-backdrop {
    position: absolute; inset: 0 0 56px 0;
    background:
      radial-gradient(ellipse at 70% 40%, rgba(255,255,255,.9) 0%, rgba(255,255,255,0) 60%),
      linear-gradient(180deg, var(--scene-top) 0%, var(--scene-mid) 60%, var(--scene-floor) 100%);
  }
  .product-photo {
    position: absolute; left: 585px; top: 100px; width: 600px; height: 470px;
    background:
      radial-gradient(circle 60px at 250px 55px, var(--product-steel) 0 70%, rgba(182,188,198,0) 100%),
      radial-gradient(circle 120px at 150px 240px, var(--product-navy) 0 80%, rgba(44,59,104,0) 100%),
      radial-gradient(circle 90px at 500px 170px, var(--product-navy) 0 78%, rgba(44,59,104,0) 100%),
      radial-gradient(circle 105px at 330px 340px, var(--product-iron) 0 80%, rgba(43,43,46,0) 100%);
  }

  .site-header { position: absolute; top: 0; left: 0; right: 0; height: 90px; }
  .menu-toggle { position: absolute; left: 162px; top: 37px; width: 20px; height: 16px; }
  .menu-toggle span { display: block; height: 2px; background: var(--ink-dark); border-radius: 2px; margin-bottom: 4px; }
  .brand {
    position: absolute; left: 200px; top: 18px;
    display: flex; flex-direction: column; align-items: center; gap: 8px;
    font-weight: 700; font-size: 13.5px; letter-spacing: .6px; color: var(--ink-dark);
  }
  .brand-dot { width: 34px; height: 34px; border-radius: 50%; background: var(--accent-blue); }

  .account-button {
    position: absolute; left: 936px; top: 29px; width: 104px; height: 32px;
    border: 1px solid var(--ink-dark); border-radius: 3px;
    display: flex; align-items: center; justify-content: center; gap: 6px;
    font-size: 13px; font-weight: 500; color: var(--ink-dark); text-decoration: none;
  }

  .hero-copy { position: absolute; left: 162px; top: 180px; }
  .eyebrow { display: flex; align-items: center; gap: 7px; font-size: 21px; font-weight: 400; letter-spacing: .5px; color: var(--ink-muted); }
  .rank {
    border: 1px solid var(--accent-outline); color: var(--accent-outline);
    font-weight: 700; padding: 0 4px; line-height: 25px; font-size: 19px;
  }
  .headline { font-size: 29px; font-weight: 800; letter-spacing: .4px; margin-top: 8px; }
  .tagline { font-size: 21px; font-style: italic; font-weight: 400; margin-top: 9px; color: var(--ink-muted); }

  .steps { position: absolute; left: 162px; top: 304px; width: 420px; height: 110px; }
  .step { position: absolute; top: 0; width: 140px; }
  .step-icon {
    width: 48px; height: 48px; border-radius: 50%; background: var(--ink-white);
    box-shadow: 0 0 0 1px #d3d8e0;
    border-bottom: 3px solid var(--accent-outline);
    display: flex; align-items: center; justify-content: center;
  }
  .step-num { font-size: 10.5px; margin-top: 10px; color: var(--ink-muted); }
  .step-title { font-size: 15px; font-weight: 600; line-height: 19px; margin-top: 4px; }
  .step-link { position: absolute; top: 24px; width: 52px; border-top: 1.5px dashed var(--line-soft); }

  .hero-actions { position: absolute; left: 161px; top: 440px; display: flex; gap: 14px; }
  .btn {
    height: 45px; display: flex; align-items: center; justify-content: center;
    font-size: 15px; font-weight: 600; border-radius: 2px; text-decoration: none;
  }
  .btn-primary { width: 165px; background: var(--accent-blue); color: var(--ink-white); }
  .btn-outline { width: 120px; border: 1px solid var(--ink-dark); font-weight: 500; color: var(--ink-dark); }

  .site-footer {
    position: absolute; left: 0; right: 0; bottom: 0; height: 56px; background: var(--footer-bg);
    display: flex; align-items: center; padding: 0 161px 0 161px; justify-content: space-between;
    color: var(--ink-white);
  }
  .copyright { font-size: 13.5px; font-weight: 400; letter-spacing: .2px; }
  .social-links { display: flex; gap: 6px; }
  .social-links span { width: 26px; height: 26px; border-radius: 50%; border: 1.5px solid var(--ink-white); }
  .social-links span.filled { background: var(--ink-white); }
</style>
</head>
<body>
<div class="page">
  <div class="hero-backdrop" role="img" aria-label="Light, softly lit grey studio backdrop with a pale floor"></div>
  <div class="product-photo" role="img" aria-label="Product photo of a swivel caster with a navy polyurethane wheel, a loose navy wheel and a black cast iron V-groove wheel"></div>

  <header class="site-header">
    <div class="menu-toggle" aria-label="Menu"><span></span><span></span><span></span></div>
    <div class="brand"><span class="brand-dot"></span><span>PIVOTS &amp; TREADS.com</span></div>
    <a class="account-button" href="#">
      <svg width="10" height="11" viewBox="0 0 10 11" aria-hidden="true"><circle cx="5" cy="3" r="2.6" fill="#1b2233"/><path d="M0 11c0-3 2-4.6 5-4.6S10 8 10 11z" fill="#1b2233"/></svg>
      Account
    </a>
  </header>

  <section class="hero-copy">
    <div class="eyebrow"><span class="rank">#1</span><span>SOLUTIONS FOR</span></div>
    <h1 class="headline">ALL YOUR APPLICATIONS.</h1>
    <p class="tagline">Easy as 1-2-3</p>
  </section>

  <section class="steps">
    <div class="step" style="left:0">
      <div class="step-icon">
        <svg width="26" height="26" viewBox="0 0 26 26" fill="none" stroke="#1f6fd6" stroke-width="1.4"><rect x="5" y="3" width="13" height="18" rx="1"/><path d="M8 8h7M8 11h7M8 14h4"/><circle cx="19" cy="18" r="4"/><path d="M17.5 18h3"/></svg>
      </div>
      <div class="step-num">Step 01</div>
      <div class="step-title">Request<br>Quote</div>
    </div>
    <div class="step-link" style="left:64px"></div>
    <div class="step" style="left:127px">
      <div class="step-icon">
        <svg width="26" height="26" viewBox="0 0 26 26" fill="none" stroke="#1f6fd6" stroke-width="1.4"><path d="M4 11l9 7 9-7v11H4z"/><path d="M7 9V4h12v5"/><circle cx="13" cy="10" r="2.5"/></svg>
      </div>
      <div class="step-num">Step 02</div>
      <div class="step-title">Receive<br>a Quote</div>
    </div>
    <div class="step-link" style="left:191px"></div>
    <div class="step" style="left:252px">
      <div class="step-icon">
        <svg width="26" height="26" viewBox="0 0 26 26" fill="none" stroke="#1f6fd6" stroke-width="1.4"><rect x="4" y="4" width="14" height="15" rx="1"/><path d="M9 4v5l2-1.5L13 9V4M7 14h5"/><circle cx="19" cy="18" r="4"/><path d="M17 18l1.5 1.5L21 16.5"/></svg>
      </div>
      <div class="step-num">Step 03</div>
      <div class="step-title">Convert a<br>Quote to Order.</div>
    </div>
  </section>

  <div class="hero-actions">
    <a class="btn btn-primary" href="#">Receive a Quote</a>
    <a class="btn btn-outline" href="#">Catalog</a>
  </div>

  <footer class="site-footer">
    <p class="copyright">Copyright © 2022 PIVOTS &amp; TREADS.com. All Rights Reserved.</p>
    <div class="social-links" aria-label="Social links"><span></span><span class="filled"></span><span></span><span></span></div>
  </footer>
</div>
</body>
</html>
```